依頼詳細
8月の19日に宮城県南三陸町の、つばさ交流センターというところで公演を予定しています。
公演に際して、町民の方々に配布するチラシの作成を依頼させて頂きたいです。

ターゲットは、未就学児くらいの子供とその親や、高齢者の方を想定しています。

当日は公演本編の他に、お客様と出演者の交流会(お茶っこ)や、
子供たちと遊ぶ時間も設ける予定です。

明るくポップで、楽しいごきげんなイメージが伝わるようなデザインを希望します。
記載項目
【表面】

■タイトル

■場所

■入場料

■問い合わせ

■主催/協力

【裏面】

■あらすじ

■キャスト

■スタッフ

■団体紹介

サイズ
A4
ページ数
両面
希望イメージ
シンプル 複雑
単色 カラフル
暗い 明るい
日常 高級
遊び心 厳粛
未来的 伝統的
女性的 男性的
希望する色
黄・オレンジ系、ロゴマークとも調和がとれると嬉しいです。
納品ファイル
• 高解像度JPG (.jpg)
• イラストレーター形式 (.ai)
• PNG形式 (.png)
補足説明
・PDFファイルでも納品いただきたいです。
・裏面のキャストは顔写真を入れていただきたいです。データは後程お渡しします。
・7月3日までに最終データを受け取れるととても助かります!
■ 選んだ理由

民話の内容に沿ったオリジナルのイラストと、お茶っこやモロッパなど細かいところにも
こだわりをもって丁寧に作ってくださっている印象で、メンバー内で一番人気で選ばせていただきました!

■ 提案者全員のお礼・コメント

民話の内容に興味をもって作ってくださったり、お子さんやお年寄りにも見やすいように。と
工夫をしてくださったりして、どれも思いが伝わってきて嬉しくなりました!
これまでは自分たちでチラシの作成もしていたので、プロフェッショナルの手にかかると
こんな風に世界が広がるんだなと、とてもクリエイティブな部分でも刺激を受けました。
ありがとうございました!!

```html
<!DOCTYPE html>
<html lang="ja">
<head>
<meta charset="utf-8">
<title>にこにこ一家2023 南三陸公演「ばば山」</title>
<link rel="stylesheet" href="https://fonts.googleapis.com/css2?family=Dela+Gothic+One&family=M+PLUS+Rounded+1c:wght@500;800;900&display=swap">
<style>
  :root {
    --yellow: #fbe34a;
    --yellow-deep: #f6cf2a;
    --orange: #f08a1c;
    --red: #e8452f;
    --pink: #f6a5a0;
    --purple: #4b2a63;
    --ink: #1c1a1a;
    --white: #ffffff;
    --brown: #8a5a36;
  }
  * { box-sizing: border-box; margin: 0; padding: 0; }
  html, body { width: 846px; height: 1200px; overflow: hidden; background: var(--yellow); }
  body { font-family: "M PLUS Rounded 1c", sans-serif; color: var(--ink); }
  .flyer { position: relative; width: 846px; height: 1200px; overflow: hidden; background: var(--yellow); }
  .abs { position: absolute; }
  .art { position: absolute; }

  .troupe-name {
    left: 22px; top: 24px; font-weight: 900; font-size: 20px; color: var(--purple);
    display: flex; align-items: center; gap: 8px;
  }
  .troupe-name .dot { width: 18px; height: 18px; border-radius: 50%; background: var(--purple); }

  .headline { left: 0; right: 0; top: 70px; text-align: center; color: var(--red); font-weight: 900; line-height: 1.15; }
  .headline .troupe { font-size: 50px; display: block; }
  .headline .place { font-size: 50px; display: block; }

  .title {
    left: 0; right: 0; top: 250px; text-align: center; font-family: "Dela Gothic One", sans-serif;
    font-size: 180px; line-height: 1; color: var(--ink); letter-spacing: 6px;
  }
  .subtitle {
    left: 0; right: 0; top: 458px; text-align: center; font-weight: 900; font-size: 36px; color: var(--purple);
    letter-spacing: 1px;
  }

  .free {
    left: 580px; top: 515px; width: 230px; height: 150px; background: var(--white); border: 5px solid var(--orange);
    border-radius: 18px; text-align: center; padding-top: 16px; color: var(--orange); font-weight: 900;
  }
  .free .big { font-size: 44px; display: block; line-height: 1.1; }
  .free .small { font-size: 22px; display: block; line-height: 1.35; margin-top: 6px; color: var(--red); }

  .date-box {
    left: 56px; top: 560px; width: 480px; height: 92px; background: var(--white); border-radius: 46px;
    color: var(--red); font-weight: 900; display: flex; align-items: baseline; justify-content: center; padding-top: 10px;
  }
  .date-box .num { font-size: 62px; }
  .date-box .unit { font-size: 40px; }
  .date-box .dow {
    display: inline-flex; align-items: center; justify-content: center; width: 44px; height: 44px; border-radius: 50%;
    background: var(--red); color: var(--white); font-size: 24px; margin-left: 8px; transform: translateY(-6px);
  }
  .times { left: 110px; top: 664px; font-weight: 800; font-size: 28px; line-height: 1.3; color: var(--ink); }
  .times .end { font-size: 22px; display: block; }

  .venue {
    left: 270px; top: 740px; width: 540px; height: 104px; background: var(--pink); border-radius: 14px;
    text-align: center; padding-top: 14px; color: var(--purple); font-weight: 900;
  }
  .venue .name { font-size: 28px; display: block; }
  .venue .address { font-size: 17px; font-weight: 800; display: block; margin-top: 10px; }

  .tea {
    left: 28px; top: 878px; width: 240px; height: 96px; background: var(--white); border-radius: 48px;
    text-align: center; padding-top: 18px; font-weight: 800; font-size: 19px; line-height: 1.35; color: var(--purple);
  }
  .toy-note { left: 640px; top: 896px; font-weight: 900; font-size: 22px; color: var(--purple); }

  .contact {
    left: 0; right: 0; top: 1146px; height: 54px; background: var(--white); display: flex; align-items: center;
    justify-content: center; gap: 18px; font-weight: 800; font-size: 22px; color: var(--purple);
  }
  .contact .label {
    background: var(--purple); color: var(--white); font-size: 16px; padding: 4px 12px; border-radius: 14px;
  }
  .contact .sep { color: var(--orange); }
</style>
</head>
<body>
<main class="flyer">
  <svg class="art" style="left:0;top:0" width="846" height="1146" role="img" aria-label="黄色地にオレンジの渦巻き模様の背景">
    <rect width="846" height="1146" fill="var(--yellow)"/>
  </svg>

  <div class="abs troupe-name"><span class="dot"></span>にこにこ一家</div>

  <h1 class="abs headline">
    <span class="troupe">にこにこ一家2023</span>
    <span class="place">南三陸公演</span>
  </h1>

  <svg class="art" style="left:0;top:140px" width="846" height="340" aria-hidden="true">
    <path d="M0 340 C 120 200, 260 90, 423 80 C 590 90, 730 200, 846 340 Z" fill="var(--white)"/>
  </svg>
  <div class="art" role="img" aria-label="山の上からのぞくおばあさんのイラスト"
       style="left:40px;top:170px;width:150px;height:150px;border-radius:50% 50% 10px 10px;background:linear-gradient(#b9a38c,#8f7c9c);"></div>
  <div class="art" role="img" aria-label="山の陰からのぞく三毛猫のイラスト"
       style="left:690px;top:150px;width:120px;height:130px;border-radius:40px 40px 10px 10px;background:linear-gradient(#f3efe6,#c8a070);"></div>

  <p class="abs title">ばば山</p>
  <p class="abs subtitle">民話を基にアレンジした創作演劇作品</p>

  <div class="abs date-box"><span class="num">2023</span><span class="unit">年</span><span class="num">8</span><span class="unit">月</span><span class="num">19</span><span class="unit">日</span><span class="dow">土</span></div>
  <div class="abs times">13:30 開場 / 14:00 開演<span class="end">(15:00 終演予定)</span></div>

  <div class="abs free"><span class="big">入場無料</span><span class="small">予約不要!<br>当日参加OK!</span></div>

  <div class="abs venue">
    <span class="name">南三陸町つばさ交流センター 第2研修室</span>
    <span class="address">宮城県本吉郡南三陸町志津川あおば台12-3</span>
  </div>

  <div class="abs tea">終演後、<br>お茶っこ(交流会)を<br>予定しています</div>

  <div class="art" role="img" aria-label="手を振る家族三人のイラスト"
       style="left:300px;top:870px;width:300px;height:270px;border-radius:120px 120px 0 0;background:linear-gradient(#f7b48a,#e8745a);"></div>
  <p class="abs toy-note">モロッパもあるよ!</p>
  <div class="art" role="img" aria-label="積み木のおもちゃのイラスト"
       style="left:640px;top:950px;width:170px;height:150px;border-radius:12px;background:linear-gradient(#d9b98a,var(--brown));"></div>

  <footer class="abs contact">
    <span class="label">お問い合わせ</span>
    <span>nikoniko.ikka@example.com</span>
    <span class="sep">|</span>
    <span>050-1234-5678</span>
  </footer>
</main>
</body>
</html>
```